Verdane Training Center
Golf Simulation & Character Education
Corporate
Milo Raskett
Chief Operations Officer
Brisby Center
North Charleston, SC
Milo@verdanetrainingcenter.com
verdanetrainingcenter.com
I would like for my logo design to be incorporated into the card design
logo full size of card on the back

```html
<!DOCTYPE html>
<html lang="en">
<head>
<meta charset="utf-8">
<title>Verdane Training Center — Stationery</title>
<link href="https://fonts.googleapis.com/css2?family=Oswald:wght@600&family=Open+Sans:wght@400;700&display=swap" rel="stylesheet">
<style>
  :root{
    --stage:#1d1d1f;
    --red:#c4141f;
    --red-dark:#8e0c14;
    --black:#121212;
    --white:#ffffff;
    --paper:#f6f6f6;
    --ink:#2a2a2a;
    --muted:#777777;
  }
  *{box-sizing:border-box;margin:0;padding:0}
  html,body{width:1200px;height:414px;overflow:hidden;background:var(--stage)}
  .board{position:relative;width:1200px;height:414px;font-family:"Open Sans",Arial,sans-serif;color:var(--ink)}
  .brand{font-family:"Oswald",Impact,sans-serif;font-weight:600;color:var(--red);line-height:1.05;letter-spacing:.5px}
  .hero-brand{position:absolute;left:70px;top:120px;width:240px;font-size:30px;text-transform:uppercase}
  .piece{position:absolute;overflow:hidden;box-shadow:0 4px 10px rgba(0,0,0,.5)}
  .piece svg.deco{position:absolute;inset:0;width:100%;height:100%}
  .card-front{top:222px;width:172px;height:66px;padding:8px 10px}
  .card-front.light{left:114px;background:var(--white)}
  .card-front.dark{left:294px;background:var(--black);color:var(--white)}
  .card-front .person{position:relative;font-size:7px;line-height:1.25}
  .card-front .person strong{display:block;font-size:8px}
  .card-front .contact{position:relative;margin-top:5px;font-size:5px;line-height:1.35;color:var(--muted)}
  .card-front.dark .contact{color:#bbbbbb}
  .card-front .brand{position:absolute;right:10px;top:10px;width:64px;font-size:10px;text-transform:uppercase;text-align:right}
  .card-back{top:296px;width:158px;height:84px;display:flex;flex-direction:column;align-items:center;justify-content:center;text-align:center}
  .card-back .brand{position:relative;font-size:14px;text-transform:uppercase;width:130px}
  .card-back .url{position:relative;margin-top:6px;font-size:5.5px}
  .card-back.white{left:34px;background:var(--white)}
  .card-back.red{left:198px;background:var(--red)}
  .card-back.red .brand,.card-back.red .url{color:var(--white)}
  .card-back.black{left:362px;background:var(--black)}
  .card-back.black .url{color:#cccccc}
  .letterhead{left:538px;top:24px;width:182px;height:338px;background:var(--white)}
  .letterhead .brand{position:absolute;left:14px;top:16px;width:90px;font-size:13px;text-transform:uppercase}
  .letterhead .address{position:absolute;right:14px;top:16px;font-size:5px;line-height:1.45;color:var(--ink)}
  .letterhead .address strong{font-size:5.5px}
  .envelope{left:800px;width:370px;height:160px}
  .envelope.black{top:22px;background:var(--black)}
  .envelope.red{top:110px;background:var(--red)}
  .envelope.white{top:200px;background:var(--paper)}
  .envelope .brand{position:absolute;left:18px;top:16px;width:150px;font-size:18px;text-transform:uppercase}
  .envelope.red .brand{color:var(--white)}
  .envelope .return{position:absolute;left:18px;top:64px;font-size:6px;line-height:1.4;color:var(--muted)}
  .envelope.red .return{color:#f2d0d2}
</style>
</head>
<body>
<main class="board">

  <div class="brand hero-brand">Verdane Training Center</div>

  <!-- business card fronts -->
  <section class="piece card-front light">
    <svg class="deco" viewBox="0 0 172 66" preserveAspectRatio="none"><path d="M100 66 C130 50 155 40 172 20 L172 66 Z" fill="var(--red)"/></svg>
    <div class="person"><strong>Milo Raskett</strong>Chief Operations Officer</div>
    <div class="contact">Office (843) 555-0192<br>Milo@verdanetrainingcenter.com<br>Brisby Center, North Charleston, SC</div>
    <div class="brand">Verdane Training Center</div>
  </section>
  <section class="piece card-front dark">
    <svg class="deco" viewBox="0 0 172 66" preserveAspectRatio="none"><path d="M100 66 C130 50 155 40 172 20 L172 66 Z" fill="var(--red)"/></svg>
    <div class="person"><strong>Milo Raskett</strong>Chief Operations Officer</div>
    <div class="contact">Mobile (843) 555-0147<br>Milo@verdanetrainingcenter.com<br>Brisby Center, North Charleston, SC</div>
    <div class="brand">Verdane Training Center</div>
  </section>

  <!-- business card backs -->
  <section class="piece card-back white">
    <div class="brand">Verdane Training Center</div>
    <div class="url">verdanetrainingcenter.com</div>
  </section>
  <section class="piece card-back red">
    <div class="brand">Verdane Training Center</div>
    <div class="url">verdanetrainingcenter.com</div>
  </section>
  <section class="piece card-back black">
    <div class="brand">Verdane Training Center</div>
    <div class="url">verdanetrainingcenter.com</div>
  </section>

  <!-- letterhead -->
  <section class="piece letterhead">
    <svg class="deco" viewBox="0 0 182 338" preserveAspectRatio="none">
      <path d="M0 338 L0 300 C40 320 80 330 120 338 Z" fill="var(--red)"/>
      <path d="M0 338 L0 318 C30 328 50 334 70 338 Z" fill="var(--black)"/>
    </svg>
    <div class="brand">Verdane Training Center</div>
    <div class="address"><strong>Brisby Center</strong><br>North Charleston, SC<br>Milo@verdanetrainingcenter.com<br>verdanetrainingcenter.com</div>
  </section>

  <!-- envelopes -->
  <section class="piece envelope black">
    <svg class="deco" viewBox="0 0 370 160" preserveAspectRatio="none">
      <path d="M0 0 L185 80 L370 0" fill="none" stroke="#2c2c2c" stroke-width="2"/>
      <path d="M200 160 C260 120 320 90 370 40 L370 160 Z" fill="var(--red)"/>
    </svg>
  </section>
  <section class="piece envelope red">
    <svg class="deco" viewBox="0 0 370 160" preserveAspectRatio="none">
      <path d="M200 160 C260 120 320 90 370 40 L370 160 Z" fill="var(--black)"/>
    </svg>
    <div class="brand">Verdane Training Center</div>
    <div class="return">Brisby Center<br>North Charleston, SC</div>
  </section>
  <section class="piece envelope white">
    <svg class="deco" viewBox="0 0 370 160" preserveAspectRatio="none">
      <path d="M230 160 C280 130 330 100 370 60 L370 160 Z" fill="var(--red)"/>
      <path d="M290 160 C320 140 350 120 370 100 L370 160 Z" fill="var(--black)"/>
    </svg>
    <div class="brand">Verdane Training Center</div>
    <div class="return">Brisby Center<br>North Charleston, SC</div>
  </section>

</main>
</body>
</html>
```